Single Page Timetracking Dashboard Desktop App UI Design (Figma Link required)

Main Idea: a SaaS tool where employees can add their time and project in a playful way. There is a infographics and a list with tasks as well.

Based on the attached concept.png the brief is following:

- check the attached rough scribble
- add own ideas or change things if they add value
- Style: colourful, nerdy, professional saas, modern, beautiful, white space
- Quality expectation: inspiration1+2.png
- I will need a Figma link
- desktop only
- make something fresh and unique

Process:
I need to include 2-3 feedback rounds that will span probably around 7 days

Target Market(s)

Internal Business Tool for a Software Development Company

Industry/Entity Type

IT

Other font styles liked:
• Could be monospace, not a must though

Requirements
Must have
• At least one page; Figma Link to the design;
Nice to have
• Microinterations like drop-down, hover/active colors; functionality specifications
Should not have
• Mobile view

```html
<!DOCTYPE html>
<html lang="en">
<head>
<meta charset="utf-8">
<title>Timetracking Dashboard</title>
<link href="https://fonts.googleapis.com/css2?family=Poppins:wght@400;500;600;700&display=swap" rel="stylesheet">
<style>
:root{
  --orange:#ff5c1f;
  --orange-soft:#ff9a3d;
  --purple:#5a45c6;
  --purple-deep:#4a36b8;
  --lilac:#ebe7fb;
  --peach:#fde9df;
  --yellow:#ffd400;
  --cream:#fdf3e0;
  --ink:#1c1b2e;
  --muted:#6f7085;
  --line:#e4e5ee;
  --page:#f6f7fb;
  --white:#ffffff;
  --blue:#3a49d8;
}
*{box-sizing:border-box;margin:0;padding:0}
html,body{width:1200px;height:2620px;overflow:hidden}
body{font-family:"Poppins",sans-serif;color:var(--ink);background:var(--page);display:flex}
svg{display:block}

.sidebar{width:86px;height:2620px;background:var(--white);border-right:1px solid var(--line);position:relative;padding-top:70px}
.nav-item{height:66px;display:flex;align-items:center;justify-content:center;margin-bottom:6px;color:#8a8b99}
.nav-item.active{background:var(--peach);border-right:5px solid var(--orange)}
.logout{position:absolute;bottom:70px;left:0;width:86px;display:flex;justify-content:center}

.content{flex:1;padding:80px 60px 0 70px}

.section-head{position:relative;height:76px;margin-bottom:40px}
.section-head .bar{position:absolute;left:0;right:0;top:22px;height:54px;background:var(--white);display:flex;align-items:center;padding-left:112px;padding-right:18px;justify-content:space-between}
.section-head .badge{position:absolute;left:26px;top:0;width:70px;height:70px;display:flex;align-items:center;justify-content:center;z-index:1}
.section-head h2{font-size:21px;font-weight:600;letter-spacing:.2px}
.badge.purple{background:var(--purple)}
.badge.orange{background:var(--orange)}
.badge.yellow{background:var(--yellow)}
.title-purple{color:var(--purple)}

.tracker{background:var(--white);border-radius:14px;height:430px;padding:36px 30px;display:flex;gap:30px;margin-bottom:90px}
.tracker-left{width:420px;display:flex;flex-direction:column}
.tracker-top{display:flex;gap:28px}
.calendar{width:196px}
.cal-head{display:flex;justify-content:space-between;align-items:center;font-size:13px;font-weight:500;margin-bottom:14px}
.cal-head span.arrow{color:#c4c5d0;font-size:11px}
.cal-grid{display:grid;grid-template-columns:repeat(7,28px);row-gap:12px;text-align:center;font-size:10px}
.cal-grid .dow{font-size:8.5px;color:var(--muted)}
.cal-grid .d{height:26px;line-height:26px;position:relative}
.cal-grid .d.hl{background:var(--orange-soft);color:var(--white);border-radius:5px}
.cal-grid .d.today{background:#ececf2;border-radius:5px}
.cal-grid .d.today::after{content:"";position:absolute;top:-3px;right:2px;width:6px;height:6px;border-radius:50%;background:var(--purple-deep)}
.cal-grid .d.out{color:#b7b8c4}

.picker{flex:1}
.select{height:30px;background:#f3f4f9;border-radius:5px;display:flex;align-items:center;justify-content:space-between;padding:0 14px;font-size:10.5px;margin-bottom:10px}
.entries{margin-top:20px;padding-right:22px}
.entry{display:flex;font-size:9.5px;color:var(--purple);padding:10px 6px;border-bottom:1px solid var(--line);white-space:nowrap}
.entry span:first-child{width:64px}
.entry:last-child{border-bottom:none}

.note{margin-top:auto;height:76px;background:#f4f5fa;border-radius:6px;padding:14px 18px;font-size:12px;display:flex;gap:10px;align-items:flex-start}

.tracker-right{flex:1;padding-left:14px}
.hours{display:grid;grid-template-columns:repeat(4,1fr);gap:14px 12px}
.hbtn{height:54px;border:1.5px solid #b8bde6;border-radius:5px;display:flex;align-items:center;justify-content:center;font-size:10.5px;font-weight:500}
.hbtn.on{background:var(--purple);border-color:var(--purple);color:var(--white);font-weight:400}
.and{text-align:center;font-size:10px;font-weight:600;margin:12px 0}
.total-row{display:flex;align-items:center;justify-content:space-between;margin-top:26px}
.total{display:flex;align-items:center;gap:12px;color:var(--purple);font-size:34px;font-weight:500}
.save{width:200px;height:74px;background:var(--orange);border-radius:5px;color:var(--white);font-size:12px;font-weight:600;display:flex;align-items:center;justify-content:center;letter-spacing:.5px}

.dropdown{height:30px;border:1px solid var(--line);border-radius:6px;padding:0 12px 0 22px;display:flex;align-items:center;gap:18px;font-size:10px;background:var(--white)}

.stats{display:flex;gap:26px;margin-bottom:50px}
.stat-card{height:300px;border-radius:14px;padding:30px 32px 0 60px;position:relative}
.stat-card.current{width:488px;background:var(--orange);color:var(--white)}
.stat-card.month{flex:1;background:var(--lilac);padding-left:48px;padding-right:22px}
.stat-top{display:flex;justify-content:space-between;align-items:center;font-size:15px}
.stat-total{display:flex;align-items:center;gap:10px;font-weight:600;font-size:15px}
.stat-total .ico{width:24px;height:24px;background:var(--white);border-radius:4px;display:flex;align-items:center;justify-content:center}
.month .stat-total{color:var(--orange)}
.stat-body{display:flex;align-items:center;margin-top:26px}
.pie{width:124px;height:124px;border-radius:50%;flex:none}
.pie.a{background:conic-gradient(from 0deg,var(--cream) 0 120deg,var(--yellow) 120deg 160deg,var(--purple) 160deg 360deg)}
.pie.b{background:conic-gradient(from 0deg,#ff9a2e 0 115deg,var(--yellow) 115deg 160deg,var(--purple) 160deg 360deg)}
.legend{margin-left:18px;font-size:12.5px}
.legend .row{display:flex;align-items:center;height:24px;white-space:nowrap}
.legend .h{width:58px}
.legend .c{width:88px}
.track{width:78px;height:5px;border-radius:3px;background:var(--white);position:relative}
.track i{position:absolute;left:0;top:0;bottom:0;border-radius:3px;background:var(--blue)}
.month .track{background:#f8f7fe}
.month .track i{background:var(--purple)}
.legend .p{margin-left:10px;width:32px}
.current .legend{margin-top:60px}

.link{display:flex;justify-content:center;align-items:center;gap:8px;color:var(--blue);font-size:12.5px;margin-bottom:90px}

.filter{height:32px;border:1px solid var(--line);border-radius:6px;padding:0 26px;display:flex;align-items:center;gap:8px;font-size:10px;background:var(--white)}

.timeline{position:relative;padding-left:34px;margin-top:30px}
.timeline::before{content:"";position:absolute;left:10px;top:26px;bottom:60px;border-left:1.5px dashed #8a8b99}
.day{display:flex;justify-content:space-between;align-items:center;margin-left:-34px;margin-bottom:24px}
.day-name{display:flex;align-items:center;gap:12px;font-size:19px;font-weight:600}
.day-total{color:var(--orange);font-size:19px;font-weight:600;padding-right:12px}
.task{margin-bottom:50px}
.task-head{height:58px;background:var(--peach);display:flex;align-items:center;justify-content:space-between;padding:0 34px}
.task-head h3{font-size:21px;font-weight:500}
.task-actions{display:flex;gap:22px}
.task-body{background:var(--white);padding:32px 20px 34px 30px;display:flex;justify-content:space-between;align-items:flex-end}
.task-meta{display:flex;align-items:center;gap:10px;font-size:15px}
.task-meta b{font-weight:600;margin-right:40px}
.task-desc{font-size:12.5px;color:var(--muted);margin-top:14px}
.task-time{text-align:right}
.task-time strong{display:block;color:var(--orange);font-size:21px;font-weight:500}
.task-time span{font-size:14.5px}
.day-gap{height:30px}
.show-all{margin-top:60px}
</style>
</head>
<body>

<aside class="sidebar">
  <div class="nav-item active">
    <svg width="28" height="28" viewBox="0 0 28 28"><circle cx="14" cy="14" r="13" fill="#ff5c1f"/><path d="M14 7v7l-3 3" stroke="#fff" stroke-width="2.2" fill="none" stroke-linecap="round"/></svg>
  </div>
  <div class="nav-item">
    <svg width="30" height="30" viewBox="0 0 30 30"><path d="M13 3a12 12 0 1 0 12 14H13z" fill="#8a8b99"/><path d="M16 1v13h13A13 13 0 0 0 16 1z" fill="#8a8b99"/></svg>
  </div>
  <div class="nav-item">
    <svg width="26" height="26" viewBox="0 0 26 26"><rect x="1" y="1" width="24" height="24" rx="5" fill="#8a8b99"/><path d="M6 9l2 2 3-3M6 17l2 2 3-3M14 10h6M14 18h6" stroke="#fff" stroke-width="1.8" fill="none" stroke-linecap="round"/></svg>
  </div>
  <div class="nav-item">
    <svg width="26" height="30" viewBox="0 0 26 30"><circle cx="13" cy="8" r="7" fill="#8a8b99"/><path d="M0 30c0-9 6-13 13-13s13 4 13 13z" fill="#8a8b99"/></svg>
  </div>
  <div class="logout">
    <svg width="26" height="26" viewBox="0 0 26 26" fill="none" stroke="#7c7d8c" stroke-width="1.8" stroke-linecap="round"><path d="M22 13H9M14 8l-5 5 5 5"/><path d="M3 3h19v20H3z"/></svg>
  </div>
</aside>

<main class="content">

  <section class="section-head">
    <div class="badge purple">
      <svg width="38" height="38" viewBox="0 0 38 38"><circle cx="19" cy="19" r="17" fill="#fff"/><path d="M19 10v9l5 4" stroke="#5a45c6" stroke-width="2.6" fill="none" stroke-linecap="round"/></svg>
    </div>
    <div class="bar"><h2>TRACK YOUR TIME</h2></div>
  </section>

  <section class="tracker">
    <div class="tracker-left">
      <div class="tracker-top">
        <div class="calendar">
          <div class="cal-head"><span class="arrow">◀</span>September 2020<span class="arrow">▶</span></div>
          <div class="cal-grid">
            <span class="dow">Mon</span><span class="dow">Tue</span><span class="dow">Wed</span><span class="dow">Thu</span><span class="dow">Fri</span><span class="dow">Sat</span><span class="dow">Sun</span>
            <span class="d">1</span><span class="d">2</span><span class="d hl">3</span><span class="d">4</span><span class="d hl">5</span><span class="d">6</span><span class="d">7</span>
            <span class="d">8</span><span class="d">9</span><span class="d">10</span><span class="d">11</span><span class="d">12</span><span class="d">13</span><span class="d">14</span>
            <span class="d">15</span><span class="d hl">16</span><span class="d">17</span><span class="d">18</span><span class="d">19</span><span class="d">20</span><span class="d">21</span>
            <span class="d">22</span><span class="d">23</span><span class="d">24</span><span class="d">25</span><span class="d">26</span><span class="d today">27</span><span class="d">28</span>
            <span class="d">29</span><span class="d">30</span><span class="d">31</span><span class="d out">1</span><span class="d out">2</span><span class="d out">3</span><span class="d out">4</span>
          </div>
        </div>
        <div class="picker">
          <div class="select">Select project<svg width="10" height="6" viewBox="0 0 10 6"><path d="M1 1l4 4 4-4" stroke="#1c1b2e" stroke-width="1.4" fill="none"/></svg></div>
          <div class="select">Select type<svg width="10" height="6" viewBox="0 0 10 6"><path d="M1 1l4 4 4-4" stroke="#1c1b2e" stroke-width="1.4" fill="none"/></svg></div>
          <div class="entries">
            <div class="entry"><span>Lena Ortiz</span><span>Collecting Data</span></div>
            <div class="entry"><span>Tomas RK</span><span>Call customer</span></div>
            <div class="entry"><span>Elise</span><span>Collect administra...</span></div>
            <div class="entry"><span>Noor Vale...</span><span>Find supplier for...</span></div>
          </div>
        </div>
      </div>
      <div class="note">
        <svg width="14" height="14" viewBox="0 0 14 14"><path d="M2 10l7-7 2 2-7 7H2z" fill="#1c1b2e"/><path d="M1 13h12" stroke="#1c1b2e" stroke-width="1.2"/></svg>
        What did you do?
      </div>
    </div>

    <div class="tracker-right">
      <div class="hours">
        <div class="hbtn on">1h</div><div class="hbtn">2h</div><div class="hbtn">3h</div><div class="hbtn">4h</div>
        <div class="hbtn">5h</div><div class="hbtn">6h</div><div class="hbtn">7h</div><div class="hbtn">8h</div>
      </div>
      <div class="and">AND</div>
      <div class="hours">
        <div class="hbtn">0m</div><div class="hbtn on">15m</div><div class="hbtn">30m</div><div class="hbtn">45</div>
      </div>
      <div class="total-row">
        <div class="total">
          <svg width="40" height="40" viewBox="0 0 40 40" fill="none" stroke="#5a45c6" stroke-width="3" stroke-linecap="round"><path d="M20 3a17 17 0 1 1-15 9" stroke-dasharray="4 3"/><path d="M20 3a17 17 0 0 1 0 34"/><path d="M20 11v10l6 4"/></svg>
          1h 15m
        </div>
        <div class="save">SAVE</div>
      </div>
    </div>
  </section>

  <section class="section-head">
    <div class="badge orange">
      <svg width="40" height="40" viewBox="0 0 40 40"><path d="M17 5a16 16 0 1 0 17 18H17z" fill="#fff"/><path d="M21 2v17h17A17 17 0 0 0 21 2z" fill="#fff"/></svg>
    </div>
    <div class="bar">
      <h2 class="title-purple">STATISTIC</h2>
      <div class="dropdown">Monate<svg width="10" height="6" viewBox="0 0 10 6"><path d="M1 1l4 4 4-4" stroke="#1c1b2e" stroke-width="1.4" fill="none"/></svg></div>
    </div>
  </section>

  <section class="stats">
    <div class="stat-card current">
      <div class="stat-top">
        <span>Current Month</span>
        <span class="stat-total"><span class="ico"><svg width="16" height="16" viewBox="0 0 16 16"><circle cx="8" cy="8" r="7" fill="#3a49d8"/><path d="M8 4v4l2 2" stroke="#fff" stroke-width="1.5" fill="none"/></svg></span>Total: 50:5 h</span>
      </div>
      <div class="stat-body">
        <div class="pie a" role="img" aria-label="Pie chart of hours per customer this month"></div>
        <div class="legend">
          <div class="row"><span class="h">40:45 h</span><span class="c">Customer A</span><span class="track"><i style="width:89%"></i></span><span class="p">89%</span></div>
          <div class="row"><span class="h">08:45 h</span><span class="c">Customer B</span><span class="track"><i style="width:78%"></i></span><span class="p">78%</span></div>
        </div>
      </div>
    </div>
    <div class="stat-card month">
      <div class="stat-top">
        <span>September</span>
        <span class="stat-total"><span class="ico"><svg width="16" height="16" viewBox="0 0 16 16"><circle cx="8" cy="8" r="7" fill="#3a49d8"/><path d="M8 4v4l2 2" stroke="#fff" stroke-width="1.5" fill="none"/></svg></span>Gesamt: 114:00 h</span>
      </div>
      <div class="stat-body">
        <div class="pie b" role="img" aria-label="Pie chart of hours per customer in September"></div>
        <div class="legend">
          <div class="row"><span class="h">40:45 h</span><span class="c">Customer A</span><span class="track"><i style="width:89%"></i></span><span class="p">89%</span></div>
          <div class="row"><span class="h">08:45 h</span><span class="c">Customer B</span><span class="track"><i style="width:78%"></i></span><span class="p">78%</span></div>
          <div class="row"><span class="h">08:45 h</span><span class="c">Customer C</span><span class="track"><i style="width:13%"></i></span><span class="p">13%</span></div>
          <div class="row"><span class="h">08:45 h</span><span class="c">Customer C</span><span class="track"><i style="width:4%"></i></span><span class="p">2%</span></div>
          <div class="row"><span class="h">08:45 h</span><span class="c">Customer D</span><span class="track"><i style="width:50%"></i></span><span class="p">55%</span></div>
        </div>
      </div>
    </div>
  </section>

  <div class="link">View all <svg width="14" height="12" viewBox="0 0 14 12" fill="none" stroke="#3a49d8" stroke-width="1.5"><path d="M1 6h11M7 1l5 5-5 5"/></svg></div>

  <section class="section-head">
    <div class="badge yellow">
      <svg width="34" height="34" viewBox="0 0 34 34"><rect x="2" y="2" width="30" height="30" rx="7" fill="#fff3a8"/><path d="M8 12l2 2 4-4M8 22l2 2 4-4M18 12h8M18 22h8" stroke="#fff" stroke-width="2" fill="none" stroke-linecap="round"/></svg>
    </div>
    <div class="bar">
      <h2 class="title-purple">YOUR TASK</h2>
      <div class="filter"><svg width="14" height="12" viewBox="0 0 14 12" fill="none" stroke="#1c1b2e" stroke-width="1.2"><path d="M1 3h12M1 9h12"/><circle cx="5" cy="3" r="2" fill="#fff"/><circle cx="9" cy="9" r="2" fill="#fff"/></svg>Filter</div>
    </div>
  </section>

  <section class="timeline">
    <div class="day">
      <div class="day-name"><svg width="22" height="22" viewBox="0 0 22 22" fill="none" stroke="#1c1b2e" stroke-width="1.6"><rect x="2" y="4" width="18" height="16" rx="2"/><path d="M6 1v5M16 1v5M5 10h2M10 10h2M15 10h2M5 15h2M10 15h2M15 15h2"/></svg>WEDNESDAY</div>
      <div class="day-total">7H 30M</div>
    </div>
    <article class="task">
      <div class="task-head"><h3>Coding</h3>
        <div class="task-actions">
          <svg width="22" height="22" viewBox="0 0 22 22" fill="none" stroke="#5a45c6" stroke-width="1.6"><path d="M4 18l1-5 10-10 4 4-10 10z"/><path d="M2 21h18"/></svg>
          <svg width="20" height="22" viewBox="0 0 20 22" fill="none" stroke="#5a45c6" stroke-width="1.6"><path d="M2 5h16M7 5V2h6v3M4 5l1 15h10l1-15"/></svg>
        </div>
      </div>
      <div class="task-body">
        <div>
          <div class="task-meta"><svg width="18" height="18" viewBox="0 0 18 18" fill="none" stroke="#6f7085" stroke-width="1.4"><circle cx="9" cy="6" r="4"/><path d="M2 17c0-4 3-6 7-6s7 2 7 6z"/></svg><b>Customer A</b>Project 1</div>
          <p class="task-desc">Lorem ipsum dolor sit amet consectetur. Amet velit tristique non urna eget orci ornare pulvinar.</p>
        </div>
        <div class="task-time"><strong>4h 30m</strong><span>December 9th</span></div>
      </div>
    </article>

    <div class="day-gap"></div>
    <div class="day">
      <div class="day-name"><svg width="22" height="22" viewBox="0 0 22 22" fill="none" stroke="#1c1b2e" stroke-width="1.6"><rect x="2" y="4" width="18" height="16" rx="2"/><path d="M6 1v5M16 1v5M5 10h2M10 10h2M15 10h2M5 15h2M10 15h2M15 15h2"/></svg>WEDNESDAY</div>
      <div class="day-total">7H 30M</div>
    </div>
    <article class="task">
      <div class="task-head"><h3>Coding</h3>
        <div class="task-actions">
          <svg width="22" height="22" viewBox="0 0 22 22" fill="none" stroke="#5a45c6" stroke-width="1.6"><path d="M4 18l1-5 10-10 4 4-10 10z"/><path d="M2 21h18"/></svg>
          <svg width="20" height="22" viewBox="0 0 20 22" fill="none" stroke="#5a45c6" stroke-width="1.6"><path d="M2 5h16M7 5V2h6v3M4 5l1 15h10l1-15"/></svg>
        </div>
      </div>
      <div class="task-body">
        <div>
          <div class="task-meta"><svg width="18" height="18" viewBox="0 0 18 18" fill="none" stroke="#6f7085" stroke-width="1.4"><circle cx="9" cy="6" r="4"/><path d="M2 17c0-4 3-6 7-6s7 2 7 6z"/></svg><b>Customer A</b>Project 1</div>
          <p class="task-desc">Lorem ipsum dolor sit amet consectetur. Amet velit tristique non urna eget orci ornare pulvinar.</p>
        </div>
        <div class="task-time"><strong>4h 30m</strong><span>December 9th</span></div>
      </div>
    </article>
    <article class="task">
      <div class="task-head"><h3>Coding</h3>
        <div class="task-actions">
          <svg width="22" height="22" viewBox="0 0 22 22" fill="none" stroke="#5a45c6" stroke-width="1.6"><path d="M4 18l1-5 10-10 4 4-10 10z"/><path d="M2 21h18"/></svg>
          <svg width="20" height="22" viewBox="0 0 20 22" fill="none" stroke="#5a45c6" stroke-width="1.6"><path d="M2 5h16M7 5V2h6v3M4 5l1 15h10l1-15"/></svg>
        </div>
      </div>
      <div class="task-body">
        <div>
          <div class="task-meta"><svg width="18" height="18" viewBox="0 0 18 18" fill="none" stroke="#6f7085" stroke-width="1.4"><circle cx="9" cy="6" r="4"/><path d="M2 17c0-4 3-6 7-6s7 2 7 6z"/></svg><b>Customer A</b>Project 1</div>
          <p class="task-desc">Lorem ipsum dolor sit amet consectetur. Amet velit tristique non urna eget orci ornare pulvinar.</p>
        </div>
        <div class="task-time"><strong>4h 30m</strong><span>December 9th</span></div>
      </div>
    </article>
  </section>

  <div class="link show-all">SHow all <svg width="14" height="12" viewBox="0 0 14 12" fill="none" stroke="#3a49d8" stroke-width="1.5"><path d="M1 6h11M7 1l5 5-5 5"/></svg></div>

</main>
</body>
</html>
```